property investment and development company needs a website

we need a website that looks professional and portrays trust for people looking to us to buy their house or investors looking to invest or joint venture with us.
We are based in the west midlands in the UK.
we deal mainly with residential housing, house to flats conversions, HMO's (houses in multiple ocupancy).
we require the website as a first point of contact with potential sellers, renters and investors so links or contact details that are easy to access or see would be good.
I have had logos designed by a brisk easel member and these can be used as guidance for the colour and style of the site.
Target Market(s)
joint venture investment partners, people looking to sell their house, people looking to rent from us.
Coding
Coded - Design and coding required
Number of Pages Required
3 page
Requirements
Must have
- project a professional appearance
- visable contact details

```html
<!DOCTYPE html>
<html lang="en">
<head>
<meta charset="utf-8">
<title>Calder Homes – Property Development and Investment</title>
<link href="https://fonts.googleapis.com/css2?family=Playfair+Display:wght@400;700&family=Open+Sans:wght@400;600;700&display=swap" rel="stylesheet">
<style>
:root{
  --gold:#c9a86a;
  --gold-dark:#b8965a;
  --navy:#232b3b;
  --navy-deep:#1d2433;
  --ink:#2a2f3a;
  --muted:#8a8f99;
  --page:#f5f6f9;
  --white:#ffffff;
  --line:#d9dbe0;
  --rent:#2ecc40;
  --sale:#f5a623;
  --price:#e0413a;
}
*{margin:0;padding:0;box-sizing:border-box}
html,body{width:1200px;height:3163px;overflow:hidden}
body{background:var(--page);font-family:"Open Sans",Arial,sans-serif;color:var(--ink);position:relative}
h1,h2{font-weight:400}
.abs{position:absolute}

/* header */
.site-header{position:absolute;left:0;top:0;width:1200px;height:120px;background:var(--page)}
.brand{position:absolute;left:88px;top:34px;display:flex;align-items:center;gap:12px}
.brand-mark{width:44px;height:44px;border-radius:50%;background:var(--gold)}
.brand-name{font-family:"Open Sans",Arial,sans-serif;font-weight:600;font-size:22px;color:var(--navy);white-space:nowrap}
.top-call{position:absolute;left:797px;top:22px;font-size:15px;color:var(--gold);font-weight:600}
.social-top{position:absolute;left:998px;top:22px;display:flex;gap:16px}
.social-top span{width:16px;height:16px;border:2px solid var(--navy)}
.social-top span:first-child{border-color:var(--gold)}
.main-nav{position:absolute;top:70px;left:395px;font-size:11px;font-weight:600;color:var(--navy)}
.main-nav a{color:inherit;text-decoration:none;position:absolute;white-space:nowrap}
.main-nav .active{color:var(--gold)}
.btn-appoint{position:absolute;left:952px;top:64px;width:160px;height:32px;border-radius:16px;background:var(--gold);color:#fff;font-size:11px;font-weight:700;display:flex;align-items:center;justify-content:center}

/* hero */
.hero{position:absolute;left:0;top:120px;width:1200px;height:480px;background:linear-gradient(100deg,#5d6a7a 0%,#8c8f8e 35%,#6e645a 60%,#a08f7c 100%)}
.hero::after{content:"";position:absolute;inset:0;background:rgba(25,30,40,.35)}
.hero-title{position:absolute;z-index:2;left:0;width:1200px;top:155px;text-align:center;color:#fff;font-family:"Playfair Display",Georgia,serif;font-weight:400;font-size:40px;line-height:46px}
.hero-tabs{position:absolute;z-index:2;top:278px;left:400px;display:flex;gap:22px}
.hero-tabs span{width:118px;height:34px;border-radius:17px;background:#fff;color:var(--navy);font-size:12px;font-weight:600;display:flex;align-items:center;justify-content:center}
.hero-tabs .on{background:var(--gold);color:#fff}
.hero-arrow{position:absolute;z-index:2;top:218px;width:28px;height:28px;border:2px solid #fff;border-radius:50%}
.hero-dots{position:absolute;z-index:2;top:430px;left:570px;display:flex;gap:6px}
.hero-dots i{width:11px;height:11px;border:2px solid #fff;border-radius:50%;display:block}
.hero-dots i:first-child{background:#fff}

/* feature rows */
.emblem{position:absolute;width:76px;height:76px;border-radius:50%;background:var(--gold)}
.sec-title{position:absolute;font-family:"Playfair Display",Georgia,serif;font-weight:400;font-size:22px;color:var(--navy);display:flex;align-items:center;gap:16px}
.sec-title::after{content:"";width:80px;height:1px;background:var(--gold)}
.body-copy{position:absolute;width:335px;font-size:12.5px;line-height:19px;color:var(--muted)}
.btn{position:absolute;height:33px;border-radius:17px;font-size:11px;font-weight:700;display:flex;align-items:center;justify-content:center;color:var(--navy);border:2px solid var(--gold);background:transparent}
.btn.fill{background:var(--gold);color:#fff}
.photo{position:absolute}

/* about */
.about{position:absolute;left:0;top:1409px;width:1200px;height:527px;background:linear-gradient(135deg,#1f2636 0%,#2b3345 45%,#222a3a 70%,#2a3244 100%)}
.about .emblem{left:562px;top:90px}
.about-title{position:absolute;top:190px;left:0;width:1200px;display:flex;justify-content:center;align-items:center;gap:20px;color:#fff;font-family:"Playfair Display",Georgia,serif;font-weight:400;font-size:34px}
.about-title::before,.about-title::after{content:"";width:75px;height:2px;background:#fff}
.about-copy{position:absolute;top:250px;left:240px;width:720px;text-align:center;color:#b6bac4;font-size:13px;line-height:20px}
.about-copy p+p{margin-top:18px}
.about .btn{left:537px;top:411px;width:126px;color:var(--gold)}

/* featured */
.feat-title{position:absolute;left:88px;top:2020px;font-family:"Playfair Display",Georgia,serif;font-weight:400;font-size:22px;color:var(--navy);display:flex;align-items:center;gap:16px}
.feat-title::after{content:"";width:80px;height:1px;background:var(--gold)}
.filters{position:absolute;left:720px;top:2030px;font-size:10px;color:var(--navy);font-weight:600;letter-spacing:.5px}
.filters span{position:absolute;white-space:nowrap}
.card{position:absolute;top:2097px;width:320px;height:396px;background:#fff;box-shadow:0 4px 14px rgba(0,0,0,.06)}
.card.lift{box-shadow:0 8px 22px rgba(0,0,0,.14)}
.card-img{height:200px}
.badge{position:absolute;left:0;top:0;padding:4px 9px;font-size:10px;font-weight:700;color:#fff;background:var(--rent)}
.badge.sale{background:var(--sale)}
.card h3{position:absolute;left:24px;top:222px;font-size:15px;font-weight:600;color:var(--navy)}
.card .addr{position:absolute;left:24px;top:246px;font-size:10.5px;color:var(--muted)}
.specs{position:absolute;left:24px;top:285px;display:flex;gap:26px;font-size:10.5px;color:var(--muted)}
.specs span{display:flex;align-items:center;gap:7px}
.card .btn{left:24px;top:336px;width:114px}
.price{position:absolute;left:152px;top:342px;font-family:"Playfair Display",Georgia,serif;font-size:15px;color:var(--price)}
.car-arrow{position:absolute;top:2283px;width:14px;height:14px}

/* footer */
.site-footer{position:absolute;left:0;top:2569px;width:1200px;height:594px;background:linear-gradient(160deg,#2a3446 0%,#1f2738 55%,#253042 100%)}
.foot-h{position:absolute;top:115px;font-family:"Playfair Display",Georgia,serif;font-weight:400;font-size:27px;color:#fff}
.field{position:absolute;height:31px;border:1px solid #6d7585;color:#c5c9d2;font-size:10.5px;padding:8px 9px}
.divider{position:absolute;left:602px;top:60px;width:1px;height:330px;background:#5a6273}
.call{position:absolute;left:664px;top:176px;color:#fff;font-size:23px;font-weight:600}
.mobile{position:absolute;left:664px;top:210px;color:#fff;font-size:13px}
.label{position:absolute;left:664px;color:var(--gold);font-size:15px;font-weight:600}
.addr-foot{position:absolute;left:664px;top:280px;color:#fff;font-size:13px;line-height:20px}
.social-foot{position:absolute;left:664px;top:377px;display:flex;gap:18px}
.social-foot span{width:18px;height:18px;border:2px solid #fff}
.foot-mark{position:absolute;left:88px;top:478px;width:66px;height:66px;border-radius:50%;background:var(--gold)}
.copy{position:absolute;left:0;width:1200px;text-align:center;color:#fff;font-size:11.5px}
.copy em{font-style:normal;color:var(--gold)}
</style>
</head>
<body>

<header class="site-header">
  <div class="brand"><span class="brand-mark"></span><span class="brand-name">Calder Homes</span></div>
  <div class="top-call">Call Us: <span>01632 960418</span></div>
  <div class="social-top"><span></span><span></span><span></span><span></span></div>
  <nav class="main-nav">
    <a class="active" style="left:0">-- Home --</a>
    <a style="left:110px">About Us</a>
    <a style="left:212px">Invest</a>
    <a style="left:297px">Sell</a>
    <a style="left:365px">Property</a>
    <a style="left:466px">Contact Us</a>
  </nav>
  <div class="btn-appoint">Make An Appointment</div>
</header>

<section class="hero" role="img" aria-label="Family at a kitchen table in a bright apartment with city views">
  <span class="hero-arrow" style="left:84px"></span>
  <span class="hero-arrow" style="left:1086px"></span>
  <h1 class="hero-title">We Are a Property Development and<br>Investment Company</h1>
  <div class="hero-tabs"><span>Sellers</span><span class="on">Renters</span><span>Investors</span></div>
  <div class="hero-dots"><i></i><i></i><i></i><i></i></div>
</section>

<!-- Invest -->
<span class="emblem" style="left:88px;top:683px"></span>
<h2 class="sec-title" style="left:205px;top:682px">Invest</h2>
<p class="body-copy" style="left:205px;top:730px">We have our own portfolio and we are active investors, so our finger is on the pulse and we are currently looking for residential development investments &amp; commercial to residential conversions in cities or regional centres showing strong growth. Our experience in the industry enables us to make extremely quick and well-informed decisions ...</p>
<div class="btn fill" style="left:205px;top:937px;width:127px">Explore More</div>
<div class="btn" style="left:346px;top:937px;width:128px">Contact Us</div>
<div class="photo" style="left:617px;top:689px;width:495px;height:280px;background:linear-gradient(90deg,#2e3544 0%,#8d8a83 40%,#d9d4cc 70%,#3a4050 100%)" role="img" aria-label="Furnished bedroom with dark curtains and chandelier"></div>

<!-- Sell -->
<div class="photo" style="left:88px;top:1050px;width:496px;height:280px;background:linear-gradient(180deg,#6fa7d8 0%,#b9d3ea 45%,#e8ecee 60%,#5f7d55 100%)" role="img" aria-label="Modern white villa with palm trees and pool"></div>
<h2 class="sec-title" style="left:665px;top:1042px">Sell</h2>
<span class="emblem" style="left:1036px;top:1040px"></span>
<p class="body-copy" style="left:665px;top:1090px">We undertake the necessary market research to evaluate an option that works for all parties involved. We will help guide you to make an informed decision on how to gain the maximum realistic value.<br>For those looking to achieve a fast and professional sale to experienced investors, we provide an approach that has been proven ...</p>
<div class="btn" style="left:665px;top:1298px;width:122px">Explore More</div>
<div class="btn" style="left:802px;top:1298px;width:130px">Contact Us</div>

<!-- About -->
<section class="about">
  <span class="emblem"></span>
  <h2 class="about-title">About Us</h2>
  <div class="about-copy">
    <p>We are a property development and investment company that have our own portfolio and we are active investors who pride ourselves in expanding our business organically.</p>
    <p>We ensure that whatever your property needs are we deliver bespoke services for our clients. For investors, sellers, landlords and tenants we bring knowledge to your next property decision, allowing you to make an informed decision.</p>
  </div>
  <div class="btn">Discover More</div>
</section>

<!-- Featured -->
<h2 class="feat-title">Featured Property</h2>
<div class="filters">
  <span style="left:0;color:var(--gold)">ALL</span>
  <span style="left:40px;color:var(--muted)">/</span>
  <span style="left:72px">FOR RENT</span>
  <span style="left:150px;color:var(--muted)">/</span>
  <span style="left:178px">FOR SALE</span>
</div>
<div class="btn" style="left:1000px;top:2022px;width:112px;height:32px">View All</div>

<svg class="car-arrow" style="left:38px" viewBox="0 0 14 14"><path d="M9 2 4 7l5 5" fill="none" stroke="#232b3b" stroke-width="2"/></svg>
<svg class="car-arrow" style="left:1148px" viewBox="0 0 14 14"><path d="m5 2 5 5-5 5" fill="none" stroke="#232b3b" stroke-width="2"/></svg>

<article class="card" style="left:88px">
  <div class="card-img" role="img" aria-label="Villa living room opening onto a pool with palm trees" style="background:linear-gradient(180deg,#d98a4a 0%,#c9b08c 45%,#6e7f86 100%)"></div>
  <span class="badge">For Rent</span>
  <h3>Villa with Pool for Rent</h3>
  <p class="addr">14 Marlow Lane, Eastfield, Westshire</p>
  <div class="specs"><span><svg width="14" height="10"><rect x="1" y="3" width="12" height="6" fill="none" stroke="#c9a86a"/></svg>2 Bed</span><span><svg width="14" height="10"><path d="M1 5h12v3H1z" fill="none" stroke="#c9a86a"/></svg>2 Baths</span><span><svg width="12" height="12"><rect x="1" y="1" width="10" height="10" fill="none" stroke="#c9a86a"/></svg>1300 SqFt</span></div>
  <div class="btn">More Info</div>
  <span class="price">Price: $6000</span>
</article>

<article class="card lift" style="left:440px">
  <div class="card-img" role="img" aria-label="Two-storey suburban house with lawn under blue sky" style="background:linear-gradient(180deg,#4f8fd0 0%,#a9c8e4 40%,#c7b79e 70%,#6f8a4c 100%)"></div>
  <span class="badge">For Rent</span>
  <h3>Villa with Pool for Rent</h3>
  <p class="addr">14 Marlow Lane, Eastfield, Westshire</p>
  <div class="specs"><span><svg width="14" height="10"><rect x="1" y="3" width="12" height="6" fill="none" stroke="#c9a86a"/></svg>2 Bed</span><span><svg width="14" height="10"><path d="M1 5h12v3H1z" fill="none" stroke="#c9a86a"/></svg>2 Baths</span><span><svg width="12" height="12"><rect x="1" y="1" width="10" height="10" fill="none" stroke="#c9a86a"/></svg>1300 SqFt</span></div>
  <div class="btn fill">More Info</div>
  <span class="price">Price: $6000</span>
</article>

<article class="card" style="left:792px">
  <div class="card-img" role="img" aria-label="Modern white house among trees" style="background:linear-gradient(180deg,#b8c2c4 0%,#e9e9e6 45%,#5c6b4e 100%)"></div>
  <span class="badge sale">For Sale</span>
  <h3>Villa with Pool for Rent</h3>
  <p class="addr">14 Marlow Lane, Eastfield, Westshire</p>
  <div class="specs"><span><svg width="14" height="10"><rect x="1" y="3" width="12" height="6" fill="none" stroke="#c9a86a"/></svg>2 Bed</span><span><svg width="14" height="10"><path d="M1 5h12v3H1z" fill="none" stroke="#c9a86a"/></svg>2 Baths</span><span><svg width="12" height="12"><rect x="1" y="1" width="10" height="10" fill="none" stroke="#c9a86a"/></svg>1300 SqFt</span></div>
  <div class="btn">More Info</div>
  <span class="price">Price: $6000</span>
</article>

<!-- Footer -->
<footer class="site-footer">
  <h2 class="foot-h" style="left:88px">Send a Message</h2>
  <div class="field" style="left:88px;top:184px;width:216px">Name</div>
  <div class="field" style="left:316px;top:184px;width:216px">Email</div>
  <div class="field" style="left:88px;top:228px;width:216px">Company Name</div>
  <div class="field" style="left:316px;top:228px;width:216px">Phone</div>
  <div class="field" style="left:88px;top:272px;width:444px;height:111px">Message ...</div>
  <div class="btn fill" style="left:88px;top:382px;width:96px;height:32px">Send</div>

  <span class="divider"></span>

  <h2 class="foot-h" style="left:664px">Contact Us</h2>
  <div class="call">Call Us: 01632 960418</div>
  <div class="mobile">Mobile: 07700 900462 &nbsp;/&nbsp; E:: info@calderhomes.example</div>
  <div class="label" style="top:250px">Address:</div>
  <div class="addr-foot">12 Linden Row, Hollybrook, Westshire,<br>WS14 4AB</div>
  <div class="label" style="top:345px">Get Social</div>
  <div class="social-foot"><span></span><span></span><span></span><span></span></div>

  <span class="foot-mark"></span>
  <p class="copy" style="top:494px">© 2019 <em>Calder Homes &amp; Developments Ltd.</em> All Rights Reserved.</p>
  <p class="copy" style="top:518px">Company Number: 10483927</p>
  <svg class="abs" style="left:1102px;top:500px" width="20" height="20" viewBox="0 0 20 20"><path d="M3 17 10 3l7 14M6 12h8" fill="none" stroke="#c9a86a" stroke-width="2"/></svg>
</footer>

</body>
</html>
```